10' x 4' outdoor vinyl banner

My company prepare and sell delicious Maryland Style Gourmet Crab Cake sandwiches at public events like fairs, festivals and concerts.
We use a 10' x 10' tent to prepare and sell this sandwiches at those events. I need a 10x4 (10 feet long by 4 feet high) banner display for the top of the tent. The same design should be scalable to another 10x3 banner for the bottom of the tent.
I need a general design of a banner with a wording that should be very attention catching
The wording is: "Maryland Crab Cake Sandwiches"
I would like also to incorporate into the design a blue crab (this is the name of specific type of crab that I'm looking for, is not just a crab painted in blue)
The theme of the design should be the sea, the shoreline, maybe some fishing boat, waves, etc, in that spirit.
I would like to use a nice blue color in the background, as we are talking about the sea and marine themes.
There are some other wordings that I would like to incorporate into the banner:
A Traditional Chesapeake Bay recipe with 100% All Natural, Blue Crab Meat . . . Rich and Flavorful . . .
This type should be in smaller size, but still visible, maybe in italics or an elegant font type.
I want something simple, inviting, like my delicious sandwiches.

```html
<!DOCTYPE html>
<html lang="en">
<head>
<meta charset="utf-8">
<title>Maryland Crab Cake Sandwiches – Tent Banner</title>
<link rel="stylesheet" href="https://fonts.googleapis.com/css2?family=League+Gothic&display=swap">
<style>
  :root {
    --page-bg: #e9e7e3;
    --sky-top: #1f6fc4;
    --sky-mid: #4a9be0;
    --cloud: #dcebf7;
    --sea-deep: #1b8fc4;
    --sea-shallow: #5fd0dc;
    --surf: #d6eef0;
    --sand: #efe9e2;
    --sand-low: #e4dcd3;
    --title-dark: #0f5db8;
    --title-light: #2c9ae4;
    --title-box: #ffffff;
    --tagline: #1e90d8;
    --crab-shell: #6f8290;
    --crab-claw: #3e7fc4;
  }
  * { margin: 0; padding: 0; box-sizing: border-box; }
  html, body {
    width: 1200px;
    height: 597px;
    overflow: hidden;
    background: var(--page-bg);
  }
  .banner {
    position: absolute;
    left: 125px;
    top: 108px;
    width: 950px;
    height: 379px;
    overflow: hidden;
    box-shadow: 0 4px 14px rgba(0,0,0,0.25);
  }
  .beach-scene {
    position: absolute;
    inset: 0;
    background: linear-gradient(180deg,
      var(--sky-top) 0%,
      var(--sky-mid) 18%,
      var(--cloud) 29%,
      var(--sea-deep) 31%,
      var(--sea-deep) 48%,
      var(--sea-shallow) 66%,
      var(--surf) 75%,
      var(--sand) 82%,
      var(--sand-low) 100%);
  }
  .blue-crab {
    position: absolute;
    left: 325px;
    top: 150px;
    width: 310px;
    height: 145px;
    border-radius: 50%;
    background: radial-gradient(ellipse at center,
      var(--crab-shell) 0%,
      var(--crab-shell) 35%,
      var(--crab-claw) 60%,
      rgba(62,127,196,0) 72%);
  }
  .title {
    position: absolute;
    left: 50%;
    top: 97px;
    display: flex;
    flex-wrap: nowrap;
    gap: 6px;
    white-space: nowrap;
    transform: translateX(-50%) scaleX(0.8);
    transform-origin: center top;
    font-weight: 400;
  }
  .title-word {
    display: block;
    height: 96px;
    background: var(--title-box);
    border-radius: 16px;
    padding: 0 10px;
    font-family: "League Gothic", "Oswald", sans-serif;
    font-weight: 400;
    font-size: 104px;
    line-height: 100px;
    letter-spacing: -0.5px;
    white-space: nowrap;
    color: var(--title-dark);
  }
  .title-word span {
    background: linear-gradient(180deg, var(--title-light), var(--title-dark));
    -webkit-background-clip: text;
    background-clip: text;
    color: transparent;
  }
  .tagline {
    position: absolute;
    left: 0;
    right: 0;
    top: 318px;
    text-align: center;
    white-space: nowrap;
    font-family: "League Gothic", "Oswald", sans-serif;
    font-size: 21.5px;
    letter-spacing: 0.4px;
    color: var(--tagline);
    text-transform: uppercase;
  }
</style>
</head>
<body>
  <main class="banner">
    <div class="beach-scene" role="img" aria-label="Photo of a sunny beach: blue sky with white clouds, turquoise sea and white sand shoreline"></div>
    <div class="blue-crab" role="img" aria-label="Photo of a Chesapeake blue crab with raised red-tipped claws"></div>
    <h1 class="title">
      <span class="title-word"><span>MARYLAND</span></span>
      <span class="title-word"><span>CRAB CAKE</span></span>
      <span class="title-word"><span>SANDWICHES</span></span>
    </h1>
    <p class="tagline">A Traditional Chesapeake Bay recipe with 100%&nbsp; All Natural, Blue Crab Meat . . . Rich and Flavorful . . .</p>
  </main>
</body>
</html>
```